Design business card using existing logo.

PLEASE DO NOT USE "RED WHITE & BLACK" color combo! Thank you.

Try different color combos such as:
- Vintage colors like brown, orange, gold, blue (not all together but a combo of 1 or 3
- Blue, w/ grey, or silver or white, Blue monochromatic can work as well.
- Use monochromatic variations on back (just an idea)

- Include full name, "Quillmarsh Records" on at least one side.

Target Market(s)

Teens

Industry/Entity Type

Business

Colors
3277b5
ffc214
f04a50
f78f20

```html
<!DOCTYPE html>
<html lang="en">
<head>
<meta charset="utf-8">
<title>Quillmarsh Records – Business Card</title>
<link rel="stylesheet" href="https://fonts.googleapis.com/css2?family=Arimo:wght@400&family=Open+Sans:wght@700&display=swap">
<style>
  :root {
    --backdrop: #2b2b2b;
    --paper: #f4f4f4;
    --ink: #1a1a1a;
    --charcoal: #333333;
    --silver: #b3b3b3;
    --stripe-light: #8c8c8c;
    --stripe-dark: #666666;
    --white: #ffffff;
  }
  html, body {
    margin: 0;
    width: 1200px;
    height: 1000px;
    overflow: hidden;
    background: var(--backdrop);
  }
  .card {
    position: absolute;
    left: 269px;
    width: 661px;
    height: 396px;
    display: block;
  }
  .card--front { top: 86px; }
  .card--back { top: 528px; }
  .sans { font-family: "Arimo", Arial, sans-serif; }
  .name { font-size: 26px; fill: var(--ink); }
  .role { font-size: 12.5px; fill: var(--ink); }
  .logo-label { font-size: 15px; fill: var(--ink); }
  .contact-dark { font-size: 13px; fill: var(--ink); }
  .contact-light { font-size: 14px; fill: var(--white); }
  .brand {
    font-family: "Open Sans", Arial, sans-serif;
    font-weight: 700;
    font-size: 35px;
    fill: var(--charcoal);
  }
  .fill-paper { fill: var(--paper); }
  .fill-charcoal { fill: var(--charcoal); }
  .fill-silver { fill: var(--silver); }
  .fill-stripe-light { fill: var(--stripe-light); }
  .fill-stripe-dark { fill: var(--stripe-dark); }
  .fill-ink { fill: var(--ink); }
  .fill-white { fill: var(--white); }
</style>
</head>
<body>

<svg class="card card--front" viewBox="0 0 661 396" aria-label="Business card front">
  <rect class="fill-paper" width="661" height="396"/>
  <polygon class="fill-silver" points="294,0 661,0 661,201 437,201"/>
  <polygon class="fill-stripe-light" points="294,0 316,0 452,201 437,201"/>
  <polygon class="fill-charcoal" points="437,201 661,201 661,396 294,396"/>
  <polygon class="fill-stripe-dark" points="437,201 452,201 313,396 294,396"/>
  <polygon class="fill-charcoal" points="0,163 47,200 0,240"/>

  <text class="sans name" x="57" y="82">MARLON AVERY</text>
  <text class="sans role" x="91" y="101">MANAGING DIRECTOR</text>

  <polygon points="164,122 248,170 248,267 164,315 80,267 80,170" fill="none" stroke="#1a1a1a" stroke-width="1.5"/>
  <text class="sans logo-label" x="164" y="214" text-anchor="middle">COMPANY</text>
  <text class="sans logo-label" x="164" y="233" text-anchor="middle">LOGO</text>

  <g class="icon-pin" transform="translate(389,61)">
    <path class="fill-ink" d="M0,-14 a10,10 0 0 1 10,10 c0,7 -10,19 -10,19 c0,0 -10,-12 -10,-19 a10,10 0 0 1 10,-10z"/>
    <circle class="fill-silver" cx="0" cy="-4" r="3.5"/>
  </g>
  <text class="sans contact-dark" x="417" y="56">YOUR CITY ADDRESS</text>
  <text class="sans contact-dark" x="417" y="75">STREET LOCATION, NY CITY,USA</text>

  <g class="icon-phone" transform="translate(421,120)">
    <path d="M-6,-13 l4,-2 l4,7 l-3,3 c1,4 4,8 8,10 l3,-3 l7,4 l-2,4 c-2,2 -6,2 -10,-1 c-6,-5 -10,-10 -12,-16 c-1,-3 0,-5 1,-6z" fill="none" stroke="#1a1a1a" stroke-width="1.4"/>
  </g>
  <text class="sans contact-dark" x="447" y="117">+18 5550 2184 7731</text>
  <text class="sans contact-dark" x="447" y="133">+18 5550 6392 4408</text>

  <g class="icon-globe" transform="translate(432,266)" fill="none" stroke="#ffffff" stroke-width="1.3">
    <circle r="10"/>
    <ellipse rx="4.5" ry="10"/>
    <line x1="-10" y1="0" x2="10" y2="0"/>
    <line x1="-8.5" y1="-5" x2="8.5" y2="-5"/>
    <line x1="-8.5" y1="5" x2="8.5" y2="5"/>
  </g>
  <text class="sans contact-light" x="458" y="269">WWW.QUILLMARSHREC.COM</text>

  <g class="icon-mail" transform="translate(404,311)">
    <rect class="fill-white" width="29" height="18"/>
    <polyline points="0,0 14.5,10 29,0" fill="none" stroke="#333333" stroke-width="1.4"/>
    <polyline points="0,18 11,8" fill="none" stroke="#333333" stroke-width="1"/>
    <polyline points="29,18 18,8" fill="none" stroke="#333333" stroke-width="1"/>
  </g>
  <text class="sans contact-light" x="442" y="324">hello@quillmarshrec.com</text>
</svg>

<svg class="card card--back" viewBox="0 0 661 394" aria-label="Business card back">
  <rect class="fill-charcoal" width="661" height="394"/>
  <rect class="fill-paper" x="0" y="158" width="661" height="78"/>
  <polyline points="0,160 50,197 0,234" fill="none" stroke="#333333" stroke-width="6"/>
  <polyline points="661,160 611,197 661,234" fill="none" stroke="#333333" stroke-width="6"/>
  <text class="brand" x="330" y="209" text-anchor="middle">QUILLMARSH RECORDS</text>
</svg>

</body>
</html>
```